Personal Business Card

Looking for a clean and modern personal business card. Basically I need something catchy to give to potential clients and people I meet. I do a lot of freelancing (from DJ'ing to wedding videography, but its mostly on the event side of things) so it's more-so about selling myself rather than identifying with a company. I'm starting to meet more people that I want to work with after meeting them so I'm revamping my business cards.

I'm looking for a clean and modern design- I know that's really vague but I'm fine with anything ranging from a symbol to just a fancy version of my name.

Details I need on the front:
Dennis Kowal
dennis@denniskowal-mail.net
(555) 807-2291

On the back I'd like to have something simple like "Nice to have met you today" or "Great meeting you".

UPDATE 9/27 Noon: My apologies for not putting it up before- I'm definitely looking for full color. Doesn't have to be a rainbow but I am looking for the least amount of blank white as possible.

UPDATE 10/1: Really impressed with what I've been getting so far and I'm working on giving everyone feedback- if your design is still up then you're still in the run. Looking for something more unique and modern so please do not post something that looks like a template from Cardloom!

Target Market(s)

Mainly to give to people aged 18-35. Most of my encounters will be casual so the card should have a "young" feeling to it. I rarely do anything in the corporate world so it doesn't have to be boring. It should give the impression that I'm the one they should go to if they need what I do (again it changes every weekend so I'll probably say the "what I do" part.

Industry/Entity Type

Wedding

Requirements
Must have
• Basically the contact information listed above
Nice to have
• I really like the colors Blue, Silver, and Purple. They don't have to necessarily all be there though. I do like the look of polished metal if that makes sense.
Should not have
• A template that resembles card-loom. I'm in a point in my life where I'm working a lot of different markets/areas so the card does not need to have an address or address placeholder.

```html
<!DOCTYPE html>
<html lang="en">
<head>
<meta charset="utf-8">
<title>Dennis Kowal – Business Card</title>
<link rel="stylesheet" href="https://fonts.googleapis.com/css2?family=Bebas+Neue&display=swap">
<style>
  :root {
    --metal-light: #dfe6ef;
    --metal-mid: #b9c4d3;
    --metal-deep: #97a3b6;
    --accent-blue: #0a8fc9;
    --accent-purple: #6a3fa0;
    --band-blue: #1f6fb3;
    --band-purple: #5a3593;
    --ink-dark: #1c1c24;
    --ink-light: #ffffff;
  }
  html, body {
    margin: 0;
    padding: 0;
    width: 1200px;
    height: 720px;
    overflow: hidden;
    background: var(--metal-mid);
  }
  .card {
    position: relative;
    width: 1200px;
    height: 720px;
    overflow: hidden;
    font-family: "Bebas Neue", "Oswald", sans-serif;
    background:
      linear-gradient(115deg, rgba(255,255,255,0) 30%, rgba(255,255,255,0.45) 48%, rgba(255,255,255,0) 62%),
      linear-gradient(160deg, var(--metal-light) 0%, var(--metal-mid) 55%, var(--metal-deep) 100%);
  }
  .card__waves {
    position: absolute;
    inset: 0;
  }
  .identity {
    position: absolute;
    left: 60px;
    top: 200px;
    width: 560px;
    text-align: center;
    color: var(--ink-dark);
  }
  .identity__name {
    margin: 0;
    font-size: 116px;
    line-height: 1;
    font-weight: 400;
  }
  .identity__role {
    margin: -8px 0 0;
    font-size: 46px;
    line-height: 1;
    letter-spacing: 0.36em;
    padding-left: 0.36em;
  }
  .wordmark {
    position: absolute;
    left: 690px;
    top: 237px;
    width: 360px;
    display: flex;
    align-items: center;
    justify-content: center;
    gap: 22px;
  }
  .wordmark__dot {
    width: 70px;
    height: 70px;
    border-radius: 50%;
    background: var(--accent-purple);
  }
  .wordmark__name {
    font-size: 84px;
    line-height: 1;
    color: var(--accent-purple);
    letter-spacing: 0.04em;
  }
  .contact {
    position: absolute;
    left: 0;
    top: 572px;
    width: 1200px;
    margin: 0;
    text-align: center;
    color: var(--ink-light);
    font-size: 34px;
    line-height: 1;
    font-weight: 400;
  }
</style>
</head>
<body>
  <div class="card">
    <svg class="card__waves" width="1200" height="720" viewBox="0 0 1200 720" aria-hidden="true">
      <defs>
        <linearGradient id="band-fill" x1="0" y1="0" x2="1" y2="1">
          <stop offset="0" stop-color="var(--band-blue)"/>
          <stop offset="1" stop-color="var(--band-purple)"/>
        </linearGradient>
      </defs>
      <path class="wave-accent" fill="var(--accent-blue)"
            d="M0 453 C 220 432, 470 440, 700 493 L 0 478 Z"/>
      <path class="wave-base" fill="url(#band-fill)"
            d="M0 478 C 260 470, 480 480, 700 493 C 880 500, 1050 490, 1200 480 L 1200 720 L 0 720 Z"/>
    </svg>

    <header class="identity">
      <h1 class="identity__name">Dennis Kowal</h1>
      <p class="identity__role">Freelancer</p>
    </header>

    <div class="wordmark">
      <span class="wordmark__dot"></span>
      <span class="wordmark__name">DENNIS</span>
    </div>

    <p class="contact">P: (555) 807-2291 * dennis@denniskowal-mail.net * www.denniskowal-web.net</p>
  </div>
</body>
</html>
```